Website for Sports and Exercise Medicine Doctor with active research in stem cells therapies.

I am a sports and exercise medicine doctor with research interests in the cutting edge areas of biological therapies, most notable stem cells. None of my patients are dying of anything, and most of them come to see me to decrease their pain, so they can get back to what they want to do.

The approach i then take is to decrease their pain and support them to achieve the things they wish to achieve. Most people start at "Just make it stop hurting doc" , but I try to move them towards something more important over time.

I would like the website to be very different to other "Doctor or medical websites" in its look. No pictures of doctors in white coats and no pictures of fit old people smiling. I would potentially like the fist thing seen to be a quote:

"Less pain. Everybody wants it, but what are you going to do, once you've got it?"

(But this is only an idea, I am open to anything)

The website will need a couple of things

1. "Locations" I work
2. "Research" I am involved in
3. "Sort Me out" - Clinical information for people to access
4. "Social" - imbedded twitter and facebook
5. "Blog" - imbedded wordpress blog
6. "Bio" - the usual bio-stuff

The "Sort Me out" - pages I would like to have the functionality as seen in this site http://www.veltarion.com.au/platelet/. I intend to put disease topics into these pages (eg Achilles tehdinopathy, osteoarthritis etc etc etc). Once again I am not wedded to this but something along these lines would be good.

To give you an idea these are some sites I like
http://www.morbanquilt.com/
http://daptrine.com/
http://ovimbera.com.sg/
http://jolvaniketchup.com/
http://www.pilnorwave.com/
http://quadrisel.com/#offering
http://fennikstudio.tv/
http://norvalgate.com/
http://sablethorn.co.uk/#about

Target Market(s)

20-80 year old.
People with tendon injuries
People with osteoarthritis
People interested in stem cells
I will build the site over time to contain information on multiple sporting injuries and musculoskeletal disorders. It will also become a site for the latest on stem cell research particularly in the area of osteoarthritis.

Industry/Entity Type

Medical

Font styles to use
Sans Serif

Colors
ffffff

Requirements
Nice to have
• To give you an idea these are some sites I like
http://daptrine.com/
http://fennikstudio.tv/
http://norvalgate.com/
Should not have
• Pictures of doctors in white coats or old fit people smiling

```html
<!DOCTYPE html>
<html lang="en">
<head>
<meta charset="utf-8">
<title>Sports &amp; Exercise Medicine</title>
<link href="https://fonts.googleapis.com/css2?family=Open+Sans:ital,wght@0,400;0,600;0,700;1,400;1,600&display=swap" rel="stylesheet">
<style>
:root{
  --green:#6cbf3a;
  --green-dark:#58a52c;
  --ink:#333;
  --muted:#777;
  --line:#dcdcdc;
  --page:#f1f1f1;
  --white:#ffffff;
  --footer:#1e1e1e;
  --footer-text:#9a9a9a;
  --footer-base:#141414;
}
*{box-sizing:border-box;margin:0;padding:0}
html,body{width:800px;height:1200px;overflow:hidden}
body{font-family:"Open Sans",Arial,sans-serif;color:var(--ink);background:var(--page);position:relative;font-size:8px;line-height:1.5}
.site-header{height:75px;background:var(--white);position:relative}
.topbar{position:absolute;left:80px;top:4px;font-size:6.5px;color:var(--muted);display:flex;gap:14px}
.topbar span{display:flex;align-items:center;gap:4px}
.logo{position:absolute;left:80px;top:26px;width:118px;height:32px;background:var(--green);color:var(--white);font-weight:700;font-size:20px;line-height:32px;padding-left:14px;letter-spacing:1px}
.main-nav{position:absolute;right:80px;top:30px;display:flex}
.main-nav a{display:block;padding:8px 9px 9px;font-size:7.5px;font-weight:700;color:#444;text-decoration:none;border-bottom:3px solid transparent;border-left:1px solid #eee}
.main-nav a:first-child{border-left:none}
.main-nav a.active{border-bottom-color:var(--green);color:#222}
.hero{position:relative;height:207px;background:linear-gradient(100deg,#4f6b3a 0%,#8aa86a 30%,#b9cfa0 55%,#6f8f52 80%,#43602f 100%);overflow:hidden}
.hero-photo{position:absolute;inset:0;background:radial-gradient(ellipse 130px 180px at 220px 140px,rgba(90,110,120,.55),transparent 70%)}
.hero-quote{position:absolute;right:78px;top:38px;text-align:right;color:var(--white);font-size:22px;line-height:1.35;font-weight:400;letter-spacing:-.3px}
.hero-quote .hl{background:var(--green);padding:0 6px}
.hero-dots{position:absolute;right:82px;bottom:10px;display:flex;gap:4px}
.hero-dots i{width:7px;height:7px;border-radius:50%;background:rgba(255,255,255,.6)}
.hero-dots i.on{background:var(--white)}
.section-title{font-size:8px;font-weight:700;text-transform:uppercase;text-align:center;color:#444;letter-spacing:.4px}
.section-title::after{content:"";display:block;width:36px;height:2px;background:var(--green);margin:4px auto 0}
.intro{padding:20px 120px 0;text-align:center}
.intro p{margin-top:8px;color:var(--muted);font-size:7px}
.features{display:flex;gap:25px;margin:42px 80px 0}
.card{flex:1;background:var(--white);border:1px solid var(--line);text-align:center;padding-bottom:14px}
.card-media{height:68px;background:linear-gradient(135deg,#9a8f86,#c9bfb2 50%,#7f8c7a)}
.card-icon{width:26px;height:26px;border-radius:50%;background:var(--green);border:3px solid var(--white);margin:-13px auto 0;position:relative;display:flex;align-items:center;justify-content:center}
.card h3{font-size:9px;font-weight:600;color:var(--green);margin-top:4px}
.card p{color:var(--muted);font-size:7px;padding:4px 18px 8px}
.btn{display:inline-block;background:var(--green);color:var(--white);font-size:7px;font-weight:600;padding:4px 16px;text-decoration:none}
.columns{display:flex;gap:40px;margin:44px 80px 0}
.col-blog{width:290px}
.col-sort{flex:1}
.blog-post{display:flex;gap:10px;margin-top:26px}
.post-date{width:26px;flex:none;text-align:center}
.post-date .day{background:#333;color:var(--white);font-size:9px;font-weight:700;line-height:20px}
.post-date .mon{background:var(--green);color:var(--white);font-size:6px;line-height:12px}
.post-body h4{font-size:8px;font-weight:700}
.post-meta{font-size:6px;color:#999;margin:2px 0 4px}
.post-body p{font-size:7px;color:var(--muted)}
.post-body .more{color:var(--green);font-size:7px;font-weight:600}
.accordion{margin-top:24px;background:var(--white);border:1px solid var(--line)}
.acc-head{display:flex;justify-content:space-between;align-items:center;padding:0 10px;height:24px;font-size:7px;font-weight:700;border-top:1px solid var(--line);color:#555}
.acc-head:first-child{border-top:none}
.acc-head.open{background:var(--green);color:var(--white)}
.acc-body{padding:10px 10px 12px;font-size:7px;color:var(--muted)}
.testimonials{margin:52px 110px 0;text-align:center}
.testimonials blockquote{margin-top:12px;font-size:7px;color:var(--muted);font-style:italic}
.testimonials cite{display:block;margin-top:10px;font-style:normal;font-size:7px;color:var(--green);font-weight:700}
.testimonials cite span{color:#999;font-weight:400}
.site-footer{position:absolute;left:0;right:0;top:990px;height:185px;background:var(--footer);color:var(--footer-text);display:flex;gap:28px;padding:22px 80px 0}
.foot-col{flex:1}
.foot-col h5{color:var(--white);font-size:15px;font-weight:400;margin-bottom:8px}
.foot-col h5 b{font-weight:700}
.foot-col ul{list-style:none;font-size:7px}
.foot-col li{padding:3px 0;border-bottom:1px solid #2c2c2c;display:flex;gap:5px;align-items:center}
.foot-col li::before{content:"›";color:var(--green)}
.foot-col p{font-size:7px;line-height:1.6}
.foot-col .more{color:var(--white);font-weight:700;font-size:7.5px;display:block;margin-top:6px}
.contact-row{display:flex;gap:7px;align-items:center;font-size:7px;padding:5px 0;border-bottom:1px solid #2c2c2c}
.contact-row .ic{width:16px;height:16px;background:#333;display:flex;align-items:center;justify-content:center;flex:none}
.base-bar{position:absolute;left:0;right:0;top:1175px;height:25px;background:var(--footer-base);color:#777;font-size:6.5px;line-height:25px;padding-left:80px}
</style>
</head>
<body>
<header class="site-header">
  <div class="topbar">
    <span><svg width="7" height="7" viewBox="0 0 10 10"><path d="M2 1l2 2-1 1.5a6 6 0 0 0 2.5 2.5L7 6l2 2-1.2 1.2C4.5 9 1 5.5.8 2.2z" fill="#999"/></svg>Phone: +00 1234 5678</span>
    <span><svg width="8" height="6" viewBox="0 0 10 7"><rect x=".5" y=".5" width="9" height="6" fill="none" stroke="#999"/><path d="M.5.5l4.5 3.5L9.5.5" fill="none" stroke="#999"/></svg>Email: hello@brivanmed.example</span>
  </div>
  <div class="logo">LOGO</div>
  <nav class="main-nav">
    <a href="#" class="active">HOME</a><a href="#">ABOUT US</a><a href="#">BLOG</a><a href="#">FAQ'S ▾</a><a href="#">CONTACT</a>
  </nav>
</header>

<section class="hero">
  <div class="hero-photo" role="img" aria-label="Photo of a young runner on a sunny park path with green trees behind"></div>
  <p class="hero-quote">Less pain. Everybody wants it,<br><span class="hl">but what are you going to do,</span><br>once you've got it?"</p>
  <div class="hero-dots"><i class="on"></i><i></i><i></i><i></i></div>
</section>

<section class="intro">
  <h2 class="section-title">Consectetur adipiscing elit.</h2>
  <p>Lorem ipsum dolor sit amet, consectetur adipiscing elit, sed do eiusmod tempor incididunt ut labore et dolore magna aliqua. Ut enim ad minim veniam, quis nostrud exercitation ullamco laboris nisi ut aliquip ex ea commodo consequat.</p>
</section>

<section class="features">
  <article class="card">
    <div class="card-media" role="img" aria-label="Photo of a clinic treatment scene"></div>
    <div class="card-icon"><svg width="10" height="10" viewBox="0 0 10 10"><path d="M1 5l3 3 5-6" fill="none" stroke="#fff" stroke-width="1.6"/></svg></div>
    <h3>Lorem Ipsum</h3>
    <p>Lorem ipsum dolor sit amet, consectetur adipiscing elit, sed do eiusmod tempor.</p>
    <a class="btn" href="#">Read more</a>
  </article>
  <article class="card">
    <div class="card-media" role="img" aria-label="Photo of an athlete training"></div>
    <div class="card-icon"><svg width="10" height="10" viewBox="0 0 10 10"><path d="M1 5l3 3 5-6" fill="none" stroke="#fff" stroke-width="1.6"/></svg></div>
    <h3>Lorem Ipsum</h3>
    <p>Lorem ipsum dolor sit amet, consectetur adipiscing elit, sed do eiusmod tempor.</p>
    <a class="btn" href="#">Read more</a>
  </article>
  <article class="card">
    <div class="card-media" role="img" aria-label="Photo of a laboratory research bench"></div>
    <div class="card-icon"><svg width="10" height="10" viewBox="0 0 10 10"><path d="M1 5l3 3 5-6" fill="none" stroke="#fff" stroke-width="1.6"/></svg></div>
    <h3>Lorem Ipsum</h3>
    <p>Lorem ipsum dolor sit amet, consectetur adipiscing elit, sed do eiusmod tempor.</p>
    <a class="btn" href="#">Read more</a>
  </article>
</section>

<section class="columns">
  <div class="col-blog">
    <h2 class="section-title">Latest from blog</h2>
    <article class="blog-post">
      <div class="post-date"><div class="day">12</div><div class="mon">MAR</div></div>
      <div class="post-body">
        <h4>LOREM IPSUM</h4>
        <div class="post-meta">3 Comments</div>
        <p>Lorem ipsum dolor sit amet, consectetur adipiscing elit, sed do eiusmod tempor incididunt ut labore et dolore magna aliqua quis nostrud.</p>
        <span class="more">Read more</span>
      </div>
    </article>
    <article class="blog-post">
      <div class="post-date"><div class="day">08</div><div class="mon">MAR</div></div>
      <div class="post-body">
        <h4>LOREM IPSUM</h4>
        <div class="post-meta">5 Comments</div>
        <p>Lorem ipsum dolor sit amet, consectetur adipiscing elit, sed do eiusmod tempor incididunt ut labore et dolore magna aliqua quis nostrud.</p>
        <span class="more">Read more</span>
      </div>
    </article>
  </div>
  <div class="col-sort">
    <h2 class="section-title">Sort me out</h2>
    <div class="accordion">
      <div class="acc-head open">LOREM IPSUM DOLOR <span>−</span></div>
      <div class="acc-body">Lorem ipsum dolor sit amet, consectetur adipiscing elit, sed do eiusmod tempor incididunt ut labore et dolore magna aliqua. Ut enim ad minim veniam, quis nostrud exercitation ullamco laboris nisi ut aliquip ex ea commodo consequat. Duis aute irure dolor in reprehenderit in voluptate velit esse cillum dolore eu fugiat nulla pariatur.</div>
      <div class="acc-head">LOREM IPSUM DOLOR <span>+</span></div>
      <div class="acc-head">LOREM IPSUM DOLOR <span>+</span></div>
      <div class="acc-head">LOREM IPSUM DOLOR <span>+</span></div>
      <div class="acc-head">LOREM IPSUM DOLOR <span>+</span></div>
      <div class="acc-head">LOREM IPSUM DOLOR <span>+</span></div>
    </div>
  </div>
</section>

<section class="testimonials">
  <h2 class="section-title">Testimonials</h2>
  <blockquote>Lorem ipsum dolor sit amet, consectetur adipiscing elit, sed do eiusmod tempor incididunt ut labore et dolore magna aliqua. Ut enim ad minim veniam, quis nostrud exercitation ullamco laboris nisi ut aliquip ex ea commodo consequat duis aute irure dolor.</blockquote>
  <cite>Mara Venn <span>Quality Designer</span></cite>
</section>

<footer class="site-footer">
  <div class="foot-col">
    <h5><b>Quick</b> Links</h5>
    <ul><li>Home</li><li>About Us</li><li>Blog</li><li>FAQ</li><li>Contact Us</li></ul>
  </div>
  <div class="foot-col">
    <h5><b>My</b> work</h5>
    <p>Lorem ipsum dolor sit amet, consectetur adipiscing elit. Sed do eiusmod tempor incididunt ut labore et dolore magna aliqua, quis nostrud exercitation ullamco.</p>
    <span class="more">Read more ›</span>
  </div>
  <div class="foot-col">
    <h5><b>My</b> Research</h5>
    <p>Lorem ipsum dolor sit amet, consectetur adipiscing elit. Sed do eiusmod tempor incididunt ut labore et dolore magna aliqua, quis nostrud exercitation ullamco.</p>
    <span class="more">Read more ›</span>
  </div>
  <div class="foot-col">
    <h5><b>Our</b> Contact</h5>
    <div class="contact-row"><span class="ic"><svg width="8" height="10" viewBox="0 0 8 10"><path d="M4 10S0 5.5 0 3.5a4 4 0 0 1 8 0C8 5.5 4 10 4 10z" fill="#6cbf3a"/><circle cx="4" cy="3.6" r="1.3" fill="#333"/></svg></span>27 Quillmere Lane,<br>Ardenvale</div>
    <div class="contact-row"><span class="ic"><svg width="9" height="9" viewBox="0 0 10 10"><path d="M2 1l2 2-1 1.5a6 6 0 0 0 2.5 2.5L7 6l2 2-1.2 1.2C4.5 9 1 5.5.8 2.2z" fill="#6cbf3a"/></svg></span>Phone: +00 1234 5678</div>
    <div class="contact-row"><span class="ic"><svg width="9" height="7" viewBox="0 0 10 7"><rect x=".5" y=".5" width="9" height="6" fill="none" stroke="#6cbf3a"/><path d="M.5.5l4.5 3.5L9.5.5" fill="none" stroke="#6cbf3a"/></svg></span>hello@brivanmed.example</div>
  </div>
</footer>
<div class="base-bar">Copyright · All Rights Reserved</div>
</body>
</html>
```